Journal Cover Design Project

The Meridian Review of Rising Trade Nations is a professional journal which aims to provide an international platform for publication of original research on the emerging economies.
The journal is published three times a year and available by subscription. Currently, the cover design is the same for each issue. We are looking to redesign the cover (and interior) of our journal and would like a design that would allow us to change the color scheme for each issue or volume while maintaining a consistent design scheme.
Our design preference is simple and modern with good use of color. Many of our past publications have used abstract maps/globes but we are open to new ideas. We would need a creative way to include text on the cover, possibly a way to present the article titles or main topics for each issue. For example, we like the use of color and the general design in this image: http://www.pictavo-share.example/photos/brightmakerstudio/5120448391/lightbox/
Below is a link to our most recent issue of the journal. You can see an example of the article titles, structure, etc. The website also shows the current cover of the journal (but we do not want the new design to be based off of the current one):
http://mrt.quellpress.example/content/4/2.toc

```html
<!DOCTYPE html>
<html lang="en">
<head>
<meta charset="utf-8">
<title>Meridian Review of Rising Trade Nations — Cover</title>
<link rel="stylesheet" href="https://fonts.googleapis.com/css2?family=Oswald:wght@700&family=Josefin+Sans:wght@400&display=swap">
<style>
  :root {
    --frame-light: #ff5cf0;
    --frame-mid: #d21cc4;
    --frame-dark: #6e0068;
    --band-top: #ffffff;
    --band-bottom: #f4c8ee;
    --night: #0a0008;
    --globe-core: #2a0226;
    --globe-rim: #d31fc2;
    --box: #8c0a8c;
    --box-text: #ffffff;
    --title-ink: #1a0018;
    --title-edge: #c01ab0;
  }
  html, body {
    margin: 0;
    padding: 0;
    overflow: hidden;
    background: #ffffff;
  }
  .cover {
    position: relative;
    width: 1200px;
    height: 1012px;
    overflow: hidden;
    background: linear-gradient(135deg, var(--frame-light), var(--frame-mid) 45%, var(--frame-dark));
  }
  .cover__inner {
    position: absolute;
    left: 43px;
    top: 46px;
    width: 1114px;
    height: 922px;
    overflow: hidden;
    background: var(--night);
    border-top: 6px solid #111;
    box-shadow: inset 0 0 0 3px rgba(60, 0, 55, 0.6);
  }
  .globe-visual {
    position: absolute;
    inset: 0;
    background:
      radial-gradient(circle 450px at 585px 600px,
        rgba(120, 10, 110, 0.55) 0%,
        var(--globe-core) 45%,
        rgba(140, 10, 130, 0.85) 80%,
        var(--globe-rim) 93%,
        rgba(180, 20, 170, 0.35) 97%,
        rgba(10, 0, 8, 0) 100%),
      radial-gradient(ellipse 520px 200px at 150px 640px, rgba(230, 60, 215, 0.55), rgba(0, 0, 0, 0) 70%),
      radial-gradient(ellipse 900px 260px at 450px 900px, rgba(110, 0, 100, 0.55), rgba(0, 0, 0, 0) 70%),
      var(--night);
  }
  .masthead {
    position: absolute;
    left: 0;
    top: 0;
    width: 1114px;
    height: 210px;
  }
  .masthead__band {
    position: absolute;
    inset: 0;
  }
  .masthead__title {
    position: absolute;
    left: 0;
    top: 0;
  }
  .publisher {
    position: absolute;
    left: 866px;
    top: 64px;
    display: flex;
    align-items: center;
    gap: 12px;
    font-family: "Josefin Sans", sans-serif;
    font-weight: 400;
    font-size: 30px;
    color: var(--title-ink);
    white-space: nowrap;
  }
  .publisher__dot {
    width: 40px;
    height: 40px;
    border-radius: 50%;
    background: var(--title-ink);
  }
  .topic {
    position: absolute;
    right: 0;
    margin: 0;
    box-sizing: border-box;
    background: var(--box);
    color: var(--box-text);
    font-family: "Josefin Sans", sans-serif;
    font-weight: 400;
    line-height: 1.2;
    white-space: nowrap;
  }
  .topic--lead { left: 584px; top: 204px; height: 117px; font-size: 46px; padding: 10px 0 0 16px; }
  .topic--global { left: 788px; top: 326px; height: 102px; font-size: 29px; padding: 6px 0 0 16px; }
  .topic--ideas { left: 737px; top: 444px; height: 111px; font-size: 30px; padding: 14px 0 0 26px; }
  .topic--interviews { left: 673px; top: 571px; height: 98px; font-size: 44px; padding: 10px 0 0 10px; }
</style>
</head>
<body>
<main class="cover">
  <div class="cover__inner">
    <div class="globe-visual" role="img" aria-label="Glowing magenta night view of the Earth with a small silhouetted figure in the lower left"></div>

    <header class="masthead">
      <svg class="masthead__band" width="1114" height="210" viewBox="0 0 1114 210" aria-hidden="true">
        <defs>
          <linearGradient id="bandFade" x1="0" y1="0" x2="0" y2="1">
            <stop offset="0" stop-color="var(--band-top)"/>
            <stop offset="0.7" stop-color="#fbe8f8"/>
            <stop offset="1" stop-color="var(--band-bottom)"/>
          </linearGradient>
        </defs>
        <path d="M0 0 H1114 V150 C900 150 700 175 520 150 C340 125 160 135 0 205 Z" fill="url(#bandFade)"/>
      </svg>
      <svg class="masthead__title" width="860" height="170" viewBox="0 0 860 170">
        <text x="0" y="140" transform="skewX(-8) translate(22 0)"
              font-family="Oswald, sans-serif" font-weight="700" font-size="110"
              textLength="820" lengthAdjust="spacingAndGlyphs"
              fill="var(--title-ink)" stroke="var(--title-edge)" stroke-width="3" paint-order="stroke">Meridian Review of Rising Trade Nations</text>
      </svg>
      <div class="publisher"><span class="publisher__dot"></span><span>Quell Press</span></div>
    </header>

    <p class="topic topic--lead">World's best economic<br>magazine</p>
    <p class="topic topic--global">All about the global<br>economy</p>
    <p class="topic topic--ideas">About new<br>marketing ideas</p>
    <p class="topic topic--interviews">Exclusive interviews</p>
  </div>
</main>
</body>
</html>
```